Design the Keystone HR business card for my new business

I've just had a logo designed (attached) for my new business doing HR consulting. I'm a one person operation at this stage, my aim is to provide support and help to small to medium sized businesses with their people objectives or issues.

I'm not really into anything overly flashy, I'm not a PR or marketing agency. I'd like my card to look modern, professional and not gimmicky.

I'm thinking black front (to go with logo), double sided with details on the back, maybe in a different colour?

Logo attached in several different formats.

Front of the card to have logo and added text: People and Development Solutions

Back of the card to also feature logo in some way and say:
Megan Tulloch
PO Box (TBA)
Marrowvale QLD 4391
0438 512 976
megan@keystonehr.com.au
www.keystonehr.com.au

Target Market(s)

Small to medium businesses / business owners.

Industry/Entity Type

Marketing

Requirements
Must have
• Double sided business card.
Should not have
• Anything overly gimmicky.

```html
<!DOCTYPE html>
<html lang="en">
<head>
<meta charset="utf-8">
<title>Keystone HR – Business Card Back</title>
<link rel="stylesheet" href="https://fonts.googleapis.com/css2?family=Noto+Sans:wght@300;400&display=swap">
<style>
  :root {
    --card-black: #000000;
    --text-white: #ffffff;
    --brand-violet: #9b3fd6;
    --glow-violet: #a54be0;
    --glow-deep: #4a1370;
    --divider-grey: #2a2a2a;
  }

  * { margin: 0; padding: 0; box-sizing: border-box; }

  html, body {
    width: 1200px;
    height: 804px;
    overflow: hidden;
    background: var(--card-black);
  }

  .card-back {
    position: relative;
    width: 1200px;
    height: 804px;
    background: var(--card-black);
    font-family: "Noto Sans", sans-serif;
    color: var(--text-white);
    overflow: hidden;
  }

  .brand-glow {
    position: absolute;
    left: -140px;
    top: 330px;
    width: 660px;
    height: 620px;
    background: radial-gradient(ellipse at 38% 55%,
      rgba(165, 75, 224, 0.55) 0%,
      rgba(120, 40, 180, 0.35) 35%,
      rgba(74, 19, 112, 0.18) 58%,
      rgba(0, 0, 0, 0) 75%);
  }

  .brand-lockup {
    position: absolute;
    top: 136px;
    right: 100px;
    display: flex;
    align-items: center;
    gap: 22px;
  }

  .brand-dot {
    width: 84px;
    height: 84px;
    border-radius: 50%;
    background: var(--brand-violet);
  }

  .brand-name {
    font-weight: 300;
    font-size: 52px;
    letter-spacing: -0.5px;
    color: var(--text-white);
    line-height: 1;
  }

  .edge-rule {
    position: absolute;
    left: 1128px;
    top: 80px;
    width: 1px;
    height: 199px;
    background: var(--divider-grey);
  }

  .contact-details {
    position: absolute;
    right: 100px;
    top: 444px;
    text-align: right;
    font-weight: 400;
    font-size: 31px;
    line-height: 42.5px;
    letter-spacing: 0.6px;
    font-style: normal;
  }
</style>
</head>
<body>
  <main class="card-back">
    <div class="brand-glow" role="img" aria-label="Soft violet glow decoration in the lower left corner"></div>

    <div class="brand-lockup">
      <span class="brand-dot"></span>
      <span class="brand-name">Keystone HR</span>
    </div>

    <span class="edge-rule"></span>

    <address class="contact-details">
      <div class="contact-name">Megan Tulloch</div>
      <div class="contact-postal">PO Box (TBA)</div>
      <div class="contact-locality">Marrowvale QLD 4391</div>
      <div class="contact-phone">0438 512 976</div>
      <div class="contact-email">megan@keystonehr.com.au</div>
      <div class="contact-web">www.keystonehr.com.au</div>
    </address>
  </main>
</body>
</html>
```